Clean, creative business Wordpress Site

Our company is building a website via Wordpress and needs a clean, no fuss, modern looking design that reflects our company brand (see attached logos).

In addition, the company is a woman owned business (no middle-aged white guy stock photos please) and primarily works with the oil & gas industry. We would prefer no images with direct references to energy (rigs, windmills, solar panels, etc.). Part of our consulting is providing thought leadership around energy politics and policy so creative ways to incorporate that visually will be appreciated as well.

Site map of pages below:

Home
- About
- Team
- Expertise
- Blog

We prefer a header image that includes the company logo and easy to identify and navigate menus.

Target Market(s)

Energy professionals, Executives

Industry/Entity Type

Consulting

Font styles to use
Serif

Colors
85acd3
0255a3
cedeed
ffffff

Requirements
Must have
• Clean and easy to navigate, clear menus, simple design that reflects company logo.

```html
<!DOCTYPE html>
<html lang="en">
<head>
<meta charset="utf-8">
<title>Corvalis Energy — Home</title>
<link href="https://fonts.googleapis.com/css2?family=Cinzel:wght@400;600;700&family=Open+Sans:wght@400;600;700&display=swap" rel="stylesheet">
<style>
:root{
  --blue-deep:#0255a3;
  --blue-mid:#85acd3;
  --blue-pale:#cedeed;
  --white:#ffffff;
  --ink:#2f3338;
  --muted:#7a7f86;
  --nav:#4a4d52;
  --grey-bg:#ececec;
  --charcoal:#45484d;
  --footer:#26282c;
  --footer-deep:#1b1c1f;
}
*{box-sizing:border-box;margin:0;padding:0}
html,body{width:1200px;height:3084px;overflow:hidden}
body{font-family:"Open Sans",Arial,sans-serif;color:var(--ink);background:var(--white);position:relative}
section,header,nav,footer{position:absolute;left:0;width:1200px}

/* header */
.site-header{top:0;height:96px;background:var(--white)}
.brand{position:absolute;left:160px;top:22px;display:flex;align-items:center;gap:12px}
.brand-mark{width:40px;height:40px;border:3px solid var(--blue-deep)}
.brand-name{font-family:"Cinzel",Georgia,serif;font-weight:700;font-size:26px;color:var(--blue-deep);letter-spacing:1px;line-height:1}
.social{position:absolute;right:160px;top:10px;display:flex;gap:6px}
.social span{width:14px;height:14px;border-radius:50%;background:var(--blue-mid)}
.phone{position:absolute;right:160px;top:44px;display:flex;align-items:center;gap:8px;font-size:18px;color:var(--ink)}
.phone-icon{width:24px;height:24px;border-radius:50%;background:var(--charcoal);display:flex;align-items:center;justify-content:center}
.main-nav{top:96px;height:44px;background:var(--nav)}
.main-nav ul{list-style:none;display:flex;position:absolute;left:160px;top:0;height:44px}
.main-nav li{width:124px;text-align:center;line-height:44px;color:var(--white);font-size:14px;text-transform:uppercase;letter-spacing:.5px}
.main-nav li.active{background:var(--blue-deep)}

/* hero */
.hero{top:140px;height:500px;background:linear-gradient(180deg,#2e6fb4 0%,#6fa3d4 45%,#c9dcec 72%,#e9d9b6 100%);overflow:hidden}
.hero-copy{position:absolute;left:640px;top:176px;width:450px;text-align:right;color:var(--white)}
.hero-copy h1{font-family:"Cinzel",Georgia,serif;font-weight:400;font-size:25px;line-height:35px;white-space:nowrap}
.btn{display:inline-block;background:var(--blue-deep);color:var(--white);font-size:12px;text-transform:uppercase;padding:9px 18px;letter-spacing:.5px}
.hero-copy .btn{margin-top:18px}
.hero-arrow{position:absolute;top:220px}
.hero-dots{position:absolute;right:150px;bottom:28px;display:flex;gap:6px}
.hero-dots span{width:9px;height:9px;background:var(--white);opacity:.5}
.hero-dots span.on{opacity:1}
.accent-bar{position:absolute;left:0;top:640px;width:1200px;height:8px;background:var(--blue-deep)}

/* about */
.about{top:648px;height:472px}
.about-tab{position:absolute;left:28px;top:42px;width:56px;height:24px;background:var(--charcoal)}
.about-tab::after{content:"";position:absolute;right:-14px;top:0;width:14px;height:24px;background:var(--blue-deep)}
.about-body{position:absolute;left:160px;top:34px;width:580px}
.section-h{font-family:"Cinzel",Georgia,serif;font-size:28px;color:var(--ink);font-weight:700}
.section-h b{color:var(--blue-deep)}
.about-rule{width:580px;height:3px;background:var(--blue-deep);margin:8px 0 14px}
.lead{color:var(--blue-deep);font-weight:700;font-size:14px;line-height:20px}
.about-p{font-size:13px;color:var(--muted);line-height:20px;margin-top:8px}
.pillar{display:flex;gap:16px;margin-top:26px}
.pillar-icon{width:46px;height:46px;border-radius:50%;background:var(--blue-deep);flex:none;display:flex;align-items:center;justify-content:center}
.pillar h3{font-family:"Cinzel",Georgia,serif;font-size:20px;color:var(--ink)}
.pillar p{font-size:12px;color:var(--muted);line-height:18px;margin-top:4px}
.quick-contact{position:absolute;left:784px;top:40px;width:260px;background:var(--grey-bg);border-top:34px solid var(--charcoal);padding:16px 18px 20px}
.quick-contact h2{position:absolute;top:-28px;left:18px;font-family:"Cinzel",Georgia,serif;color:var(--white);font-size:18px;font-weight:400}
.field{height:30px;background:var(--white);border:1px solid #d6d6d6;margin-bottom:10px;font-size:12px;color:var(--muted);padding:7px 10px}
.field.tall{height:70px}
.quick-contact .btn{float:right}
.quick-contact::after{content:"";display:block;clear:both}

/* services */
.services{top:1120px;height:540px;background:var(--grey-bg)}
.title-block{text-align:center}
.title-block h2{font-family:"Cinzel",Georgia,serif;font-size:32px;color:var(--ink);font-weight:400}
.title-block h2 b{color:var(--blue-deep);font-weight:400}
.divider{display:flex;align-items:center;justify-content:center;gap:10px;margin-top:8px}
.divider i{width:300px;height:1px;background:#bfc4ca}
.divider em{width:12px;height:12px;border:2px solid var(--blue-deep);transform:rotate(45deg)}
.services .title-block{position:absolute;top:46px;width:1200px}
.service-grid{position:absolute;left:160px;top:140px;width:880px;display:grid;grid-template-columns:repeat(3,280px);gap:20px 20px}
.tile{background:var(--white);height:176px}
.tile .ph{height:136px}
.tile p{font-family:"Cinzel",Georgia,serif;text-align:center;font-size:15px;line-height:40px;color:var(--ink)}
.ph-a{background:linear-gradient(135deg,#b8c6d4,#5f7186)}
.ph-b{background:linear-gradient(135deg,#e8e3da,#9d8e7a)}
.ph-c{background:linear-gradient(135deg,#c7cfd8,#6d7c8e)}
.ph-d{background:linear-gradient(135deg,#f2e4c0,#6b5b45)}
.ph-f{background:linear-gradient(135deg,#8fb2d6,#27486f)}
.tile.promo{background:var(--blue-deep);color:var(--white);text-align:center;padding:38px 24px 0}
.tile.promo h3{font-family:"Cinzel",Georgia,serif;font-weight:400;font-size:17px;line-height:25px}
.tile.promo .btn{background:var(--white);color:var(--blue-deep);margin-top:16px;padding:7px 16px;font-size:11px}

/* why */
.why{top:1660px;height:470px}
.why .title-block{position:absolute;top:70px;width:1200px}
.why-art{position:absolute;left:0;top:130px}
.feature{position:absolute;width:200px}
.feature h4{font-family:"Cinzel",Georgia,serif;font-size:17px;color:var(--blue-deep);font-weight:600;line-height:20px}
.feature p{font-size:11px;color:var(--muted);line-height:16px;margin-top:4px}
.feature.left{text-align:right}

/* blog + testimonials */
.blog{top:2130px;height:370px;width:600px;background:var(--blue-deep);color:var(--white)}
.testimonials{top:2130px;left:600px;height:370px;width:600px;background:var(--charcoal);color:var(--white)}
.panel-h{font-family:"Cinzel",Georgia,serif;font-size:27px;font-weight:400;position:absolute;top:34px}
.panel-rule{position:absolute;top:80px;height:2px;background:var(--blue-mid)}
.post{position:absolute;left:160px;display:flex;gap:16px;width:400px}
.date{width:46px;flex:none;text-align:center;background:var(--white);color:var(--blue-deep)}
.date b{display:block;font-size:18px;line-height:26px}
.date span{display:block;background:var(--charcoal);color:var(--white);font-size:10px;line-height:16px;text-transform:uppercase}
.post h5{font-size:14px;font-weight:700}
.post p{font-size:11px;line-height:16px;margin-top:4px;color:var(--blue-pale)}
.avatar{position:absolute;left:38px;top:120px;width:80px;height:80px;border-radius:50%;background:linear-gradient(135deg,#d9c3a8,#8c6e52);border:3px solid var(--white)}
.quote{position:absolute;left:140px;top:110px;width:300px;font-size:12px;line-height:19px;color:#d4d6d9}
.quote-by{position:absolute;left:140px;top:270px;font-size:13px;font-weight:700}

/* clients */
.clients{top:2500px;height:260px}
.clients .title-block{position:absolute;top:40px;width:1200px}
.logo-row{position:absolute;left:160px;top:140px;width:880px;display:flex;justify-content:space-between;align-items:center}
.logo-row .arrow{width:30px;text-align:center}
.client{width:150px;height:74px;border:1px solid #e2e2e2;display:flex;align-items:center;justify-content:center;font-weight:700;font-size:18px;color:var(--charcoal)}

/* footer */
.site-footer{top:2760px;height:324px;background:var(--footer);color:#c7c9cc}
.footer-col{position:absolute;top:40px}
.footer-col h6{font-size:15px;color:var(--white);font-weight:600;margin-bottom:14px}
.footer-col ul{list-style:none;font-size:12px;line-height:22px}
.footer-col li::before{content:"›";color:var(--blue-mid);margin-right:8px}
.contact-line{display:flex;gap:10px;font-size:12px;line-height:17px;margin-bottom:14px}
.contact-line svg{flex:none;margin-top:2px}
.map{width:200px;height:150px;background:linear-gradient(135deg,#e6e4dc,#c9d6c4)}
.footer-brand{position:absolute;left:888px;top:60px;width:180px;display:flex;flex-direction:column;align-items:center;gap:12px}
.footer-brand i{width:90px;height:90px;border:4px solid #5b5e63}
.footer-brand span{font-family:"Cinzel",Georgia,serif;font-weight:700;font-size:20px;color:#6c7075}
.footer-social{position:absolute;top:220px;display:flex;gap:8px}
.footer-social span{width:20px;height:20px;border-radius:50%;border:1px solid #6c7075}
.copyright{position:absolute;left:0;bottom:0;width:1200px;height:44px;background:var(--footer-deep);font-size:11px;color:#8a8d92;line-height:44px;padding-left:160px}
</style>
</head>
<body>

<header class="site-header">
  <div class="brand"><span class="brand-mark"></span><span class="brand-name">Corvalis Energy</span></div>
  <div class="social"><span></span><span></span><span></span><span></span></div>
  <div class="phone">
    <span class="phone-icon"><svg width="12" height="12" viewBox="0 0 24 24"><path fill="#fff" d="M6.6 10.8a15 15 0 0 0 6.6 6.6l2.2-2.2c.3-.3.7-.4 1-.2 1.1.4 2.3.6 3.6.6.6 0 1 .4 1 1V20c0 .6-.4 1-1 1A17 17 0 0 1 3 4c0-.6.4-1 1-1h3.5c.6 0 1 .4 1 1 0 1.3.2 2.5.6 3.6.1.3 0 .7-.2 1z"/></svg></span>
    123 456 7890
  </div>
</header>

<nav class="main-nav">
  <ul><li class="active">Home</li><li>About Us</li><li>Team</li><li>Expertise</li><li>Blog</li><li>Contact</li></ul>
</nav>

<section class="hero" role="img" aria-label="Photograph of two climbers helping each other up a rock at sunset against a blue sky">
  <svg class="hero-arrow" style="left:20px" width="24" height="44" viewBox="0 0 24 44"><path d="M20 4 L4 22 L20 40" stroke="#fff" stroke-width="3" fill="none"/></svg>
  <svg class="hero-arrow" style="right:20px" width="24" height="44" viewBox="0 0 24 44"><path d="M4 4 L20 22 L4 40" stroke="#fff" stroke-width="3" fill="none"/></svg>
  <div class="hero-copy">
    <h1>We Work Closely Alongside<br>Clients To Evaluate Their<br>Needs &amp; Requirements</h1>
    <span class="btn">Free Consultation</span>
  </div>
  <div class="hero-dots"><span class="on"></span><span></span><span></span><span></span></div>
</section>
<div class="accent-bar"></div>

<section class="about">
  <div class="about-tab"></div>
  <div class="about-body">
    <h2 class="section-h">About <b>Corvalis Energy</b></h2>
    <div class="about-rule"></div>
    <p class="lead">Lorem ipsum dolor sit amet, consectetuer adipiscing elit, sed diam nonummy nibh euismod tincidunt ut laoreet dolore.</p>
    <p class="about-p">Lorem ipsum dolor sit amet, consectetuer adipiscing elit, sed diam nonummy nibh euismod tincidunt ut laoreet dolore magna aliquam erat volutpat.</p>
    <div class="pillar">
      <span class="pillar-icon"><svg width="22" height="22" viewBox="0 0 24 24"><circle cx="12" cy="12" r="9" stroke="#fff" stroke-width="2" fill="none"/><circle cx="12" cy="12" r="4" fill="#fff"/></svg></span>
      <div><h3>Our Mission</h3><p>Lorem ipsum dolor sit amet, consectetuer adipiscing elit, sed diam nonummy nibh euismod tincidunt ut laoreet dolore magna aliquam erat volutpat.</p></div>
    </div>
    <div class="pillar">
      <span class="pillar-icon"><svg width="24" height="24" viewBox="0 0 24 24"><path d="M2 12 Q12 3 22 12 Q12 21 2 12Z" stroke="#fff" stroke-width="2" fill="none"/><circle cx="12" cy="12" r="3" fill="#fff"/></svg></span>
      <div><h3>Our Vision</h3><p>Lorem ipsum dolor sit amet, consectetuer adipiscing elit, sed diam nonummy nibh euismod tincidunt ut laoreet dolore magna aliquam erat volutpat.</p></div>
    </div>
  </div>
  <form class="quick-contact">
    <h2>Quick Contact</h2>
    <div class="field">Name</div>
    <div class="field">Email</div>
    <div class="field">Phone</div>
    <div class="field tall">Message</div>
    <span class="btn">Submit Now</span>
  </form>
</section>

<section class="services">
  <div class="title-block"><h2>Our <b>Services</b></h2><div class="divider"><i></i><em></em><i></i></div></div>
  <div class="service-grid">
    <div class="tile"><div class="ph ph-a" role="img" aria-label="Photograph of people joining hands in a team circle"></div><p>Community Engagement</p></div>
    <div class="tile"><div class="ph ph-b" role="img" aria-label="Photograph of hands signing a policy document"></div><p>Navigating Policy</p></div>
    <div class="tile"><div class="ph ph-c" role="img" aria-label="Photograph of a business team in discussion"></div><p>Deescalating Conflict</p></div>
    <div class="tile"><div class="ph ph-d" role="img" aria-label="Photograph of a glowing light bulb held in a hand"></div><p>Energy Access</p></div>
    <div class="tile promo"><h3>Our Work Is Dedicated To The Prosperity Of Our Clients</h3><span class="btn">Call Us Today</span></div>
    <div class="tile"><div class="ph ph-f" role="img" aria-label="Photograph of a financial market chart on a screen"></div><p>Investor Relations</p></div>
  </div>
</section>

<section class="why">
  <div class="title-block"><h2>Why <b>Corvalis Energy</b></h2><div class="divider"><i></i><em></em><i></i></div></div>
  <svg class="why-art" width="1200" height="340" viewBox="0 0 1200 340" aria-hidden="true">
    <g fill="none" stroke="#bfc4ca" stroke-width="1.5">
      <path d="M420 70 Q520 70 548 150"/><path d="M420 270 Q520 270 548 190"/>
      <path d="M780 70 Q680 70 652 150"/><path d="M780 270 Q680 270 652 190"/>
    </g>
    <circle cx="600" cy="170" r="98" fill="#fff" stroke="#cedeed" stroke-width="6"/>
    <circle cx="600" cy="170" r="84" fill="none" stroke="#85acd3" stroke-width="1"/>
    <rect x="586" y="112" width="28" height="28" fill="none" stroke="#0255a3" stroke-width="3"/>
    <text x="600" y="180" text-anchor="middle" font-family="Cinzel, Georgia, serif" font-weight="700" font-size="19" fill="#0255a3">Corvalis</text>
    <text x="600" y="204" text-anchor="middle" font-family="Cinzel, Georgia, serif" font-weight="700" font-size="19" fill="#0255a3">Energy</text>
    <g fill="#fff" stroke="#0255a3" stroke-width="2">
      <rect x="404" y="54" width="32" height="32" transform="rotate(45 420 70)"/>
      <rect x="404" y="254" width="32" height="32" transform="rotate(45 420 270)"/>
      <rect x="764" y="54" width="32" height="32" transform="rotate(45 780 70)"/>
      <rect x="764" y="254" width="32" height="32" transform="rotate(45 780 270)"/>
    </g>
    <g stroke="#0255a3" stroke-width="2" fill="none">
      <circle cx="420" cy="70" r="7"/><path d="M420 66 L420 70 L423 72"/>
      <path d="M414 270 L419 275 L427 265"/>
      <path d="M775 63 L783 70 L775 77"/>
      <path d="M773 272 Q780 262 787 272"/><circle cx="780" cy="264" r="3"/>
    </g>
  </svg>
  <div class="feature left" style="left:196px;top:175px"><h4>Years of Experience</h4><p>Lorem ipsum dolor sit amet, consectetuer adipiscing sed elit.</p></div>
  <div class="feature left" style="left:196px;top:375px"><h4>Certified Experts</h4><p>Lorem ipsum dolor sit amet, consectetuer adipiscing sed elit.</p></div>
  <div class="feature" style="left:804px;top:175px"><h4>Fast Work and Help</h4><p>Lorem ipsum dolor sit amet, consectetuer adipiscing sed elit.</p></div>
  <div class="feature" style="left:804px;top:375px"><h4>Satisfied Clients</h4><p>Lorem ipsum dolor sit amet, consectetuer adipiscing sed elit.</p></div>
</section>

<section class="blog">
  <h2 class="panel-h" style="left:160px">Latest Blog Posts</h2>
  <div class="panel-rule" style="left:160px;width:400px"></div>
  <article class="post" style="top:116px">
    <div class="date"><b>06</b><span>Jan</span></div>
    <div><h5>Diam Nonummy Nibh Euism Od Tincidunt</h5><p>Lorem ipsum dolor sit amet, consectetuer adipiscing elit, sed diam nonummy nibh euismod tincidunt ut laoreet dolore magna.</p></div>
  </article>
  <article class="post" style="top:236px">
    <div class="date"><b>06</b><span>Jan</span></div>
    <div><h5>Diam Nonummy Nibh Euism Od Tincidunt</h5><p>Lorem ipsum dolor sit amet, consectetuer adipiscing elit, sed diam nonummy nibh euismod tincidunt ut laoreet dolore magna.</p></div>
  </article>
</section>

<section class="testimonials">
  <h2 class="panel-h" style="left:38px">Clients Testimonials</h2>
  <div class="panel-rule" style="left:38px;width:400px"></div>
  <div class="avatar" role="img" aria-label="Portrait photograph of the client"></div>
  <p class="quote">“Lorem ipsum dolor sit amet, consectetuer adipiscing elit, sed diam nonummy nibh euismod tincidunt ut laoreet dolore magna aliquam erat volutpat. Ut wisi enim ad minim veniam, quis nostrud exerci tation ullamcorper suscipit lobortis nisl ut aliquip ex ea commodo consequat duis autem vel eum iriure.”</p>
  <p class="quote-by">– Mr. Tomas Reyer</p>
</section>

<section class="clients">
  <div class="title-block"><h2>Our <b>Clients</b></h2><div class="divider"><i></i><em></em><i></i></div></div>
  <div class="logo-row">
    <span class="arrow"><svg width="14" height="26" viewBox="0 0 14 26"><path d="M12 2 L2 13 L12 24" stroke="#7a7f86" stroke-width="2" fill="none"/></svg></span>
    <div class="client">Ferrano</div>
    <div class="client">Aquaflux</div>
    <div class="client">Helixor</div>
    <div class="client">Brandtline</div>
    <div class="client">Nordel</div>
    <span class="arrow"><svg width="14" height="26" viewBox="0 0 14 26"><path d="M2 2 L12 13 L2 24" stroke="#7a7f86" stroke-width="2" fill="none"/></svg></span>
  </div>
</section>

<footer class="site-footer">
  <div class="footer-col" style="left:160px">
    <h6>Quick Links</h6>
    <ul><li>Home</li><li>About Us</li><li>Team</li><li>Expertise</li><li>Blog</li><li>Contact</li></ul>
  </div>
  <div class="footer-col" style="left:360px;width:220px">
    <h6>Contact Detail</h6>
    <div class="contact-line"><svg width="12" height="14" viewBox="0 0 24 28"><path d="M12 0a10 10 0 0 0-10 10c0 7.5 10 18 10 18s10-10.5 10-18A10 10 0 0 0 12 0zm0 14a4 4 0 1 1 0-8 4 4 0 0 1 0 8z" fill="#85acd3"/></svg><span>Corvalis Energy<br>214 Harbor Street, Suite 8<br>Houston, TX 77002</span></div>
    <div class="contact-line"><svg width="12" height="12" viewBox="0 0 24 24"><path fill="#85acd3" d="M6.6 10.8a15 15 0 0 0 6.6 6.6l2.2-2.2c.3-.3.7-.4 1-.2 1.1.4 2.3.6 3.6.6.6 0 1 .4 1 1V20c0 .6-.4 1-1 1A17 17 0 0 1 3 4c0-.6.4-1 1-1h3.5c.6 0 1 .4 1 1 0 1.3.2 2.5.6 3.6.1.3 0 .7-.2 1z"/></svg><span>123 456 7890</span></div>
    <div class="contact-line"><svg width="13" height="10" viewBox="0 0 26 20"><rect x="1" y="1" width="24" height="18" fill="none" stroke="#85acd3" stroke-width="2"/><path d="M1 1 L13 11 L25 1" fill="none" stroke="#85acd3" stroke-width="2"/></svg><span>info@corvalisenergy.com</span></div>
  </div>
  <div class="footer-col" style="left:620px">
    <h6>Location Map</h6>
    <div class="map" role="img" aria-label="Street map showing the office location"></div>
  </div>
  <div class="footer-brand"><i></i><span>Corvalis Energy</span></div>
  <div class="footer-social" style="left:944px"><span></span><span></span><span></span></div>
  <div class="copyright">Copyright © 2017 Corvalis Energy. All Rights Reserved.</div>
</footer>

</body>
</html>
```